Gestaltung eines Merkblattes
Ein Entwurf, der genau meinen Vorstellungen entspricht. Eine Abwicklung, die schneller und professioneller nicht sein könnte. Die Kommunikation - sehr symphatisch und kundenorientiert. Resumee: Besser geht es nicht.
Zielgruppe
www.tierklang-analytik.de/ Medizinische Bioresonanzanalysen für Pferde. Die Kundschaft besteht hauptsächlich aus Frauen, Alter von 20- 55 Jahre.
Bei dem Projekt handelt es sich um die Gestaltung eines wichtigen Merkblattes, das jedem Kunde zusammen mit dem Befund der Analyse gemailt wird. Es enthält wichtige Informationen rund um die Bioresonanzanalyse und sollte als pdf- Datei vorliegen.
Aufgabenstellung
Kernproblem: Die Kunden lesen das Merkblatt gar nicht oder nicht sorgfältig. So entstehen viele Fragen in der Folge, die nicht notwendig wären.
Wir benötigen eine pdf- Datei, die zum Lesen anregt, gerne gelesen wird und in der die wichtigsten Aspekte in das Auge fallen. Diese wurden von mir in der Worddatei, die den Text enthält, rot markiert.
Der Text in schwarz ist deutlich weniger wichtig.
Ach ja, die Überschrift ist doof. 'Allgemeine Hinweise' das animiert nicht wirklich zum Lesen. Falls Sie eine griffige Idee haben, sehr gerne.

```html
<!DOCTYPE html>
<html lang="de">
<head>
<meta charset="utf-8">
<title>Das sollten Sie beachten – Merkblatt</title>
<link rel="stylesheet" href="https://fonts.googleapis.com/css2?family=Roboto:wght@400;500;700&display=swap">
<style>
  :root {
    --page: #ffffff;
    --frame: #d6d6d6;
    --green-strong: #9eb05c;
    --green-mid: #adbc74;
    --green-soft: #bec78f;
    --ink: #ffffff;
  }
  * { box-sizing: border-box; margin: 0; padding: 0; }
  html, body {
    width: 848px; height: 1200px; overflow: hidden;
    background: var(--page);
  }
  body {
    font-family: "Roboto", Arial, sans-serif;
    color: var(--ink);
    border: 1px solid var(--frame);
    position: relative;
  }
  .sheet {
    position: absolute;
    left: 20px; top: 20px;
    width: 808px; height: 1159px;
  }
  .block { position: absolute; left: 0; width: 100%; padding-left: 41px; }
  .block--essentials { top: 0; height: 587px; background: var(--green-strong); padding-top: 48px; }
  .block--retest { top: 587px; height: 202px; background: var(--green-mid); padding-top: 10px; }
  .block--flowers { top: 789px; height: 370px; background: var(--green-soft); padding-top: 16px; }

  .sheet-title {
    font-weight: 700; font-size: 41px; line-height: 48px;
    text-align: center; margin-left: -41px;
    letter-spacing: 0.2px;
  }
  .section-title {
    font-weight: 500; font-size: 24.5px; line-height: 32px;
  }
  .block--essentials .section-title { margin-top: 13px; }
  .text {
    font-size: 15.6px; line-height: 22.6px; font-weight: 400;
    white-space: nowrap; margin-bottom: 22.6px;
  }
  .text:last-child { margin-bottom: 0; }
</style>
</head>
<body>
  <main class="sheet">
    <section class="block block--essentials">
      <h1 class="sheet-title">DAS SOLLTEN SIE BEACHTEN!</h1>
      <h2 class="section-title">Das wichtigste zuerst</h2>
      <p class="text">Die empfohlenen Präparate können (wenn nicht anders angegeben) in das normale Kraftfutter<br>gegeben werden. Tropfen und Bachblüten bitte auf ein kleines Stück trockenes Brot, Zwieback,<br>bei Pferden, die kein Getreide fressen dürfen, auf ein Stück Reiswaffel geben, und dem Pferd<br>direkt füttern.</p>
      <p class="text">Vitabasis Pulver muss nicht, wie vom Hersteller angegeben, in Wasser aufgelöst werden. Eine<br>Gabe in das Kraftfutter, Heucobs etc. vermindert nicht die Wirkung.</p>
      <p class="text">Bitte füttern Sie alle Präparate, außer es sind abweichende Empfehlungen vorhanden, ohne<br>Unterbrechung, bis Ihnen das Ergebnis der ersten Nachtestung vorliegt. Pausen von mehr als<br>zwei Tagen können zu Beginn der Behandlung die positive Entwicklung Ihres Pferdes beein-<br>trächtigen.</p>
      <p class="text">Falls Ihr Pferd sehr wählerisch ist bei der Zufütterung von Präparaten in Pellets- oder Pulver-<br>form, dann beginnen Sie mit einer sehr kleinen Dosierung von z. b. ½ Teelöffel und steigern<br>diese sehr langsam. Bei trockenem Futter (Müsli, Hafer) sortieren manche Pferde gerne aus.<br>Hier ist es sinnvoll, das Futter anzu feuchten, etwas Heucobs oder getreidefreies Mash dazu-<br>zugeben.</p>
    </section>

    <section class="block block--retest">
      <h2 class="section-title">Nachtestung</h2>
      <p class="text">Wir bestätigen den Eingang der Probe zur Nachtestung nicht. In regelmäßigen Abständen<br>werden alle Befunde nachgetestet. Wir senden Ihnen im Anschluss per Mail das neue Ergebnis<br>mit einer aktualisierten Therapieempfehlung zu.</p>
      <p class="text">Wir brauchen für die Nachtestung eine neue Haarprobe und ein kurzes Feedback zu der<br>aktuellen Entwicklung Ihres Pferdes. Mehr nicht.</p>
    </section>

    <section class="block block--flowers">
      <h2 class="section-title">Bachblüten</h2>
      <p class="text">Wenn die Therapieempfehlung eine Übersicht an Bachblüten enthält, dann spiegeln diese den<br>seelischen Zustand Ihres Pferdes wieder, der von seinen aktuellen Lebensbedingungen, seiner<br>körperlichen Belastung durch Krankheit und durch Abläufe in seiner Herde beeinflusst wird.<br>Erfahrungsgemäß bezieht sich die Darstellung der Blüten bei Pferden, die in einer Herde leben,<br>häufig mehr auf die Gefühle des Pferdes gegenüber seinen Artgenossen als auf den Kontakt<br>mit dem Menschen.</p>
      <p class="text">Die meisten Apotheken kennen sich aus mit der Herstellung einer Bachblütenmischung. Falls<br>nicht, hier die Anleitung: in ein 30 ml Medizinfläschchen mit Tropfvorrichtung oder Pipette gibt<br>man 10 ml Alkohol (Brandy oder Weinbrand), 20 ml Quellwasser oder stilles Mineralwasser<br>(ohne Kohlensäure; kein destilliertes Wasser!) und 2-3 Tropfen von jeder Blüte, die im Moment<br>benötigt wird. Als Alternative zu Alkohol kann auch Obstessig eingesetzt werden.</p>
    </section>
  </main>
</body>
</html>
```